Website redesign for fast growing company looking to present a unique image

We're looking to revamp our online image to represent the professional, accomplished company we have become. We want to move beyond a templated look and feel to a custom design - we are eager to have you design a new public face for us! In particular, we need creative ways to display text to stand out. We are reaching top-level, C-suite executives and want to give them the confidence that we have the skills, talent, expertise, and knowledge to help their companies grow.
Updates

Designs look the same

Target Market(s)

contact centers, business process outsourcing

Industry/Entity Type

Call Center

Coding

Coded - Design and coding required

Number of Pages Required

4 page

Font styles to use
Sans Serif

Colors

Designer to choose colors to be used in the design.

Requirements
Must have
• Designed for a professional audience - C-suite executives - but that also shows our personality as a company that is nimble, personable, trustworthy, and smart. Must be lively, but not quirky. Professional, but not overly formal. Be bold with choices for imagery - we want to look unique so go beyond traditional "business/corporate" stock photos. Instead use imagery similar to what is on our staging website - torvenda.com/staging. Do not use the "neon" sign. Use colors to match and complement our logo - bright orange and dark blue. Creative text boxes that we can use throughout the site. I have attached pages of our current staging site to display some of the types of imagery that might work. We are looking for "professional with a personality" Note: this design will be transferred into a Wordpress framework.
Nice to have
• We like the animated text features of the Vorquin.com site - bold colors, great display of text features that break up the page and engage people to continue scrolling.
Should not have
• Cheesy stock photos of call center agents wearing headsets. Overly used stock photos of professionals in suits shaking hands, high-rise buildings, connection/network graphics. Current management does not like the neon sign graphics displayed on our staging site (torvenda.com/staging). We do not like style of sites that use cartoon-like icons and figures.

```html
<!DOCTYPE html>
<html lang="en">
<head>
<meta charset="utf-8">
<title>Torvenda — Customer Service, Tech Support and BPO</title>
<link href="https://fonts.googleapis.com/css2?family=Poppins:wght@400;500;600;700;800&family=Open+Sans:wght@400;600;700&display=swap" rel="stylesheet">
<style>
:root{
  --blue:#1c4f9c;
  --navy:#1d3c78;
  --orange:#f2671f;
  --ink:#2b2f38;
  --muted:#6d7380;
  --line:#e2e5ea;
  --grey:#f3f4f6;
  --white:#ffffff;
}
*{box-sizing:border-box;margin:0;padding:0}
html,body{width:1200px;height:5332px;overflow:hidden}
body{font-family:"Open Sans",Arial,sans-serif;color:var(--ink);background:var(--white);font-size:14px;line-height:1.55}
h1,h2,h3,h4,.brand,.btn,.num{font-family:"Poppins",Arial,sans-serif}
section,header,footer{position:relative;width:1200px;overflow:hidden}
.btn{display:inline-block;background:var(--orange);color:#fff;font-size:14px;font-weight:500;padding:11px 26px;border-radius:3px;text-decoration:none}
.btn.dark{background:var(--navy)}

/* header */
.site-header{height:80px;display:flex;align-items:center;justify-content:space-between;padding:0 80px;background:#fff;box-shadow:0 2px 8px rgba(0,0,0,.06);z-index:2}
.brand{display:flex;align-items:center;gap:10px;font-size:30px;font-weight:700;color:var(--navy);letter-spacing:.5px}
.brand-mark{width:22px;height:22px;background:var(--orange);border-radius:50%}
.nav{display:flex;gap:34px;font-size:14px;font-family:"Poppins",sans-serif;color:var(--ink)}
.nav .search{width:16px;height:16px}

/* hero */
.hero{height:480px}
.hero-art{position:absolute;right:0;top:0;width:860px;height:480px;background:radial-gradient(ellipse at 60% 45%,#9aa0a8 0%,#d9dce0 40%,#fff 75%)}
.hero-copy{position:absolute;left:110px;top:90px;width:500px}
.hero h1{color:var(--blue);font-size:46px;line-height:1.12;font-weight:700}
.hero p{font-family:"Poppins",sans-serif;color:var(--navy);font-size:19px;font-weight:500;margin:14px 0 34px;line-height:1.35}

/* intro */
.intro{height:260px;text-align:center;padding-top:95px}
.intro h2{color:var(--orange);font-size:27px;font-weight:700}
.intro p{width:720px;margin:12px auto 0;color:var(--muted);font-size:14px}

/* options */
.options{height:680px;border-top:1px solid var(--line)}
.devices{position:absolute;left:120px;top:90px;width:480px;height:360px;background:linear-gradient(160deg,#eef2f8,#c9d6ea 60%,#e6ebf3);border-radius:8px}
.options-copy{position:absolute;left:640px;top:85px;width:440px}
.options-copy h2{color:var(--blue);font-size:19px;line-height:1.4;font-weight:700;text-align:center}
.steps{margin-top:24px;display:flex;flex-direction:column;gap:14px}
.step{border:1px solid var(--line);border-radius:4px;padding:14px 18px;background:#fff;box-shadow:0 2px 6px rgba(0,0,0,.04)}
.step small{color:var(--orange);font-weight:700;font-size:12px}
.step h3{color:var(--navy);font-size:17px;font-weight:600;margin:2px 0}
.step p{font-size:12px;color:var(--muted)}

/* testimonials */
.trusted{height:700px;background:var(--grey);text-align:center;padding-top:110px}
.trusted h2{color:var(--navy);font-size:34px;font-weight:600}
.slider{position:absolute;top:230px;left:0;width:1200px;height:360px}
.quote-card{position:absolute;top:0;height:330px;background:#fff;border-radius:6px;padding:30px 42px;text-align:left;box-shadow:0 4px 14px rgba(0,0,0,.06)}
.quote-card.main{left:200px;width:800px}
.quote-card.side{width:150px;opacity:.5}
.quote-card.left{left:-110px}.quote-card.right{left:1160px}
.qmark{font-family:"Poppins",sans-serif;font-size:64px;line-height:.8;color:#c8ccd3}
.quote-card p{color:var(--muted);font-size:14px;margin-top:10px}
.quote-card h4{color:var(--navy);font-size:19px;margin-top:22px}
.quote-card .role{font-size:12px;color:var(--muted)}
.arrow{position:absolute;top:140px;width:44px;height:44px;border-radius:50%;display:flex;align-items:center;justify-content:center}
.arrow.prev{left:168px;background:#8d9199}.arrow.next{left:988px;background:var(--blue)}
.dots{position:absolute;top:600px;left:0;width:1200px;display:flex;justify-content:center;gap:8px}
.dots span{width:9px;height:9px;border-radius:50%;background:#c5c9cf}.dots span:first-child{background:var(--blue)}

/* better */
.better{height:800px;text-align:center}
.better h2{color:var(--navy);font-size:36px;font-weight:700;margin-top:65px}
.better .sub{font-size:14px;color:var(--muted)}
.side-btns{position:absolute;right:52px;top:30px;display:flex;flex-direction:column;gap:14px}
.side-btns .btn{width:130px;text-align:center;padding:10px 0}
.arc{position:absolute;left:0;top:0}
.point{position:absolute;width:170px;text-align:center;transform:translateX(-50%)}
.circle{margin:0 auto;width:100px;height:100px;border-radius:50%;background:var(--blue);color:#fff;font-family:"Poppins",sans-serif;font-size:34px;font-weight:600;display:flex;align-items:center;justify-content:center;border:6px solid #fff;box-shadow:0 0 0 2px #d3dbe8}
.circle.hot{background:var(--orange)}
.point h3{font-size:17px;color:var(--navy);font-weight:600;margin-top:8px}
.point.hot h3{color:var(--orange)}
.point p{font-size:11px;color:var(--muted);line-height:1.4}
.desk{position:absolute;left:150px;top:450px;width:900px;height:290px;background:linear-gradient(180deg,#fff 0%,#eef1f5 55%,#dde2e8 100%)}

/* market */
.market{height:640px;background:var(--grey)}
.market-head{text-align:center;padding-top:45px}
.market-head h2{color:var(--navy);font-size:36px;font-weight:700}
.market-head p{color:var(--muted);font-size:14px}
.tabs{position:absolute;top:160px;left:110px;width:980px;display:flex;border-bottom:2px solid var(--line);font-family:"Poppins",sans-serif;font-size:14px}
.tabs span{padding:6px 20px;color:var(--ink)}
.tabs span+span{border-left:1px solid #cfd3da}
.tabs .on{background:var(--orange);color:#fff}
.focus{position:absolute;top:235px;left:110px;width:520px}
.focus h3{color:var(--blue);font-size:21px;font-weight:600}
.focus>p{font-size:12px;color:var(--muted);margin:6px 0 20px}
.feature-grid{display:grid;grid-template-columns:1fr 1fr;gap:22px 40px}
.feature .num{color:var(--orange);font-size:34px;font-weight:600;line-height:1}
.feature h4{color:var(--navy);font-size:15px;font-weight:600;margin-top:4px}
.feature p{font-size:11px;color:var(--muted);line-height:1.4}
.market-photo{position:absolute;top:230px;left:740px;width:360px;height:370px;background:linear-gradient(150deg,#b9a48c,#7d6a58 50%,#d9d3c8);border-radius:2px}

/* benefits */
.benefits{height:640px}
.building{position:absolute;left:110px;top:70px;width:440px;height:520px;background:linear-gradient(170deg,#b3c6dd,#5f7ea6 55%,#34496b)}
.badge{position:absolute;left:430px;top:400px;width:150px;height:150px;border-radius:50%;background:var(--navy);border:6px solid #fff;color:#fff;text-align:center;display:flex;flex-direction:column;justify-content:center;font-family:"Poppins",sans-serif}
.badge b{font-size:44px;line-height:1}.badge span{font-size:14px}
.benefit-copy{position:absolute;left:640px;top:95px;width:460px}
.benefit-copy h2{color:var(--navy);font-size:36px;line-height:1.2;font-weight:700}
.benefit-list{list-style:none;margin-top:28px;display:flex;flex-direction:column;gap:12px}
.benefit-list li{display:flex;gap:12px;font-size:14px;color:var(--muted)}
.benefit-list b{color:var(--ink)}
.tick{flex:0 0 18px;height:18px;margin-top:2px}

/* economics */
.economics{height:580px;text-align:center}
.economics h2{color:var(--navy);font-size:34px;font-weight:700;margin-top:30px}
.economics .lead{width:560px;margin:6px auto 0;font-size:13px;color:var(--muted)}
.ebook-card{position:absolute;left:125px;top:150px;width:950px;height:400px;background:#fff;border-radius:6px;box-shadow:0 6px 24px rgba(0,0,0,.12);text-align:left}
.ebook{position:absolute;left:30px;top:25px;width:380px;height:350px;background:#fff;border:1px solid var(--line)}
.ebook-top{height:80px;background:var(--navy);color:#fff;padding:16px 20px;font-family:"Poppins",sans-serif;font-size:16px;font-weight:600;line-height:1.25}
.ebook-text{padding:14px 20px;font-size:10px;color:var(--muted);line-height:1.45}
.ebook-img{position:absolute;right:20px;top:100px;width:120px;height:110px;background:linear-gradient(160deg,#dde3ea,#aab6c4)}
.form{position:absolute;left:470px;top:30px;width:440px}
.form h3{color:var(--navy);font-size:23px;font-weight:600;margin-bottom:10px}
.field{display:flex;justify-content:space-between;align-items:center;border-bottom:1px solid #cfd3da;padding:14px 2px;font-size:13px;color:#9aa0a8}
.field.filled{color:var(--blue);font-size:16px}
.form .btn{margin-top:26px;margin-left:-24px}

/* footer */
.site-footer{height:472px;background:var(--navy);color:#fff}
.footer-grid{position:absolute;top:80px;left:110px;width:980px;display:grid;grid-template-columns:300px 170px 170px 1fr;gap:20px}
.site-footer h4{font-size:15px;font-weight:600;margin-bottom:10px}
.site-footer p,.site-footer li{font-size:12px;color:#c9d3e6;line-height:1.9}
.site-footer ul{list-style:none}
.social{display:flex;gap:8px;margin-top:18px}
.social span{width:20px;height:20px;border-radius:50%;background:#fff;opacity:.9}
.cta h3{font-family:"Poppins",sans-serif;font-size:20px;line-height:1.3;font-weight:600;margin-bottom:20px}
.footer-bar{position:absolute;bottom:0;left:0;width:1200px;height:50px;background:#173366;display:flex;justify-content:space-between;align-items:center;padding:0 110px;font-size:12px;color:#c9d3e6}
.to-top{position:absolute;right:50px;bottom:70px;width:30px;height:30px;border-radius:50%;background:var(--blue);border:1px solid #5c7fbd}
</style>
</head>
<body>

<header class="site-header">
  <div class="brand"><span class="brand-mark"></span>Torvenda</div>
  <nav class="nav">
    <span>Home</span><span>Markets We Serve</span><span>About Us</span><span>Contact</span><span>Apply Today</span>
    <svg class="search" viewBox="0 0 16 16" fill="none" stroke="#2b2f38" stroke-width="2"><circle cx="7" cy="7" r="5"/><path d="M11 11l4 4"/></svg>
  </nav>
</header>

<section class="hero">
  <div class="hero-art" role="img" aria-label="Flowing grey wireframe wave mesh"></div>
  <div class="hero-copy">
    <h1>Get More from Your Customer Interactions</h1>
    <p>Lift Your Top and Bottom Lines with Professional Outsourcing Solutions from Torvenda</p>
    <a class="btn">Get Started</a>
  </div>
</section>

<section class="intro">
  <h2>It's a new world are you ready?</h2>
  <p>It's time to find solutions that deliver more value. Shed the manual interactions that cost you money and distract you from your core. Get more by partnering with Torvenda for Customer Service, Tech Support, and Business Process Outsourcing solutions.</p>
</section>

<section class="options">
  <div class="devices" role="img" aria-label="Desktop, laptop, tablet and phone showing service dashboards"></div>
  <div class="options-copy">
    <h2>Flexible, versatile, end-to-end outsourcing options to help you get more of your business needs</h2>
    <div class="steps">
      <div class="step"><small>01 Step</small><h3>Customer Service Contact Center</h3><p>Improve satisfaction with trained teams and smarter, faster processes for every contact.</p></div>
      <div class="step"><small>02 Step</small><h3>Tech Support Service Center</h3><p>Ready agents for users and customers with Level 1, 2 and 3 support.</p></div>
      <div class="step"><small>03 Step</small><h3>Business Process Outsourcing</h3><p>Streamline business and back-office processes that hold your team back.</p></div>
      <div class="step"><small>04 Step</small><h3>End-to-End Solutions</h3><p>Build a new service center from the ground up with leading CRM and telephony tools.</p></div>
    </div>
  </div>
</section>

<section class="trusted">
  <h2>Trusted By Customers</h2>
  <div class="slider">
    <div class="quote-card side left"></div>
    <div class="quote-card main">
      <div class="qmark">&ldquo;</div>
      <p>Their team took over our support lines in weeks and the results were clear from the first month. Response times dropped, satisfaction scores rose and our own staff could finally focus on growth. We have a partner who listens, adapts quickly and reports openly on every measure that matters to us. It has been one of the best decisions our leadership has made in years, and we keep adding new programs to the work we share.</p>
      <h4>Dana Corwell</h4>
      <div class="role">Vice President, Customer Operations</div>
    </div>
    <div class="quote-card side right"></div>
    <div class="arrow prev"><svg width="14" height="14" viewBox="0 0 14 14" fill="none" stroke="#fff" stroke-width="2"><path d="M9 2L4 7l5 5"/></svg></div>
    <div class="arrow next"><svg width="14" height="14" viewBox="0 0 14 14" fill="none" stroke="#fff" stroke-width="2"><path d="M5 2l5 5-5 5"/></svg></div>
  </div>
  <div class="dots"><span></span><span></span><span></span></div>
</section>

<section class="better">
  <h2>Better. Faster. Leaner. Smarter</h2>
  <div class="sub">Get More from Your Customer Interactions</div>
  <div class="side-btns"><a class="btn">Contact</a><a class="btn dark">Demo</a></div>
  <div class="desk" role="img" aria-label="Bright desk with laptop showing analytics, plant and notebooks"></div>
  <svg class="arc" width="1200" height="800"><path d="M160 460 Q 600 100 1050 460" fill="none" stroke="#c7d2e4" stroke-width="2"/></svg>
  <div class="point" style="left:160px;top:410px"><div class="circle">01</div><h3>More Value</h3><p>Clear savings on every contact you send our way</p></div>
  <div class="point" style="left:320px;top:240px"><div class="circle">02</div><h3>More Performance</h3><p>Higher scores on the measures you track</p></div>
  <div class="point hot" style="left:508px;top:195px"><div class="circle hot">03</div><h3>More Focus</h3><p>Time back for the work at your core</p></div>
  <div class="point" style="left:708px;top:215px"><div class="circle">04</div><h3>More Loyalty</h3><p>Customers who stay and buy again</p></div>
  <div class="point" style="left:900px;top:240px"><div class="circle">05</div><h3>More Insights</h3><p>Reports that show what to fix next</p></div>
  <div class="point" style="left:1050px;top:410px"><div class="circle">06</div><h3>More Options</h3><p>Flexible programs that grow with you</p></div>
</section>

<section class="market">
  <div class="market-head">
    <h2>We Serve Your Market</h2>
    <p>We serve commercial businesses and federal and state government. We can serve you.</p>
  </div>
  <div class="tabs"><span class="on">Insurance</span><span>Government</span><span>Customer Service</span><span>Commercial Business</span><span>Business Process</span><span>Tech Support</span></div>
  <div class="focus">
    <h3>Focus on Your Core</h3>
    <p>Offload transactional volume and shift capital expense to outsourcing your claims, enrollment, member benefits, and customer service to Torvenda.</p>
    <div class="feature-grid">
      <div class="feature"><div class="num">01</div><h4>Claims Processing</h4><p>Improve efficiency. Supplement your team or manage the full process.</p></div>
      <div class="feature"><div class="num">02</div><h4>Enrollment Solutions</h4><p>Scale for peak seasons and manage steady state more efficiently.</p></div>
      <div class="feature"><div class="num">03</div><h4>Customer Service</h4><p>Billing, coverage, and benefit questions answered swiftly and professionally.</p></div>
      <div class="feature"><div class="num">04</div><h4>Work-from-Home</h4><p>Choose home-based agents for business continuity.</p></div>
    </div>
  </div>
  <div class="market-photo" role="img" aria-label="Professional working at a laptop in a bright office"></div>
</section>

<section class="benefits">
  <div class="building" role="img" aria-label="Company office building exterior against blue sky"></div>
  <div class="badge"><b>25</b><span>Years<br>Experience</span></div>
  <div class="benefit-copy">
    <h2>Discover the Benefits of Outsourcing</h2>
    <ul class="benefit-list">
      <li><svg class="tick" viewBox="0 0 18 18"><circle cx="9" cy="9" r="9" fill="#f2671f"/><path d="M5 9l3 3 5-6" fill="none" stroke="#fff" stroke-width="2"/></svg><span><b>Shed overhead</b> and invest in core resources.</span></li>
      <li><svg class="tick" viewBox="0 0 18 18"><circle cx="9" cy="9" r="9" fill="#f2671f"/><path d="M5 9l3 3 5-6" fill="none" stroke="#fff" stroke-width="2"/></svg><span><b>Reduce risk</b>. Lower headcount, infrastructure, and technology costs.</span></li>
      <li><svg class="tick" viewBox="0 0 18 18"><circle cx="9" cy="9" r="9" fill="#f2671f"/><path d="M5 9l3 3 5-6" fill="none" stroke="#fff" stroke-width="2"/></svg><span><b>Scale up and down</b> as needed.</span></li>
      <li><svg class="tick" viewBox="0 0 18 18"><circle cx="9" cy="9" r="9" fill="#f2671f"/><path d="M5 9l3 3 5-6" fill="none" stroke="#fff" stroke-width="2"/></svg><span><b>Focus on your business</b>, not on labor-intensive processes.</span></li>
      <li><svg class="tick" viewBox="0 0 18 18"><circle cx="9" cy="9" r="9" fill="#f2671f"/><path d="M5 9l3 3 5-6" fill="none" stroke="#fff" stroke-width="2"/></svg><span><b>Build customer affinity</b> with professional service teams.</span></li>
      <li><svg class="tick" viewBox="0 0 18 18"><circle cx="9" cy="9" r="9" fill="#f2671f"/><path d="M5 9l3 3 5-6" fill="none" stroke="#fff" stroke-width="2"/></svg><span><b>Continuous improvement</b> via performance management.</span></li>
      <li><svg class="tick" viewBox="0 0 18 18"><circle cx="9" cy="9" r="9" fill="#f2671f"/><path d="M5 9l3 3 5-6" fill="none" stroke="#fff" stroke-width="2"/></svg><span><b>Access data</b> to make better business decisions.</span></li>
    </ul>
  </div>
</section>

<section class="economics">
  <h2>The Economics of Outsourcing</h2>
  <p class="lead">Take a hard look at your operating model. What overhead and labor costs can you shed? How can you change in order to become more competitive? Our eBook shows you the way.</p>
  <div class="ebook-card">
    <div class="ebook">
      <div class="ebook-top">Calculating the<br>Economics of Outsourcing</div>
      <div class="ebook-img" role="img" aria-label="Small chart photo on ebook page"></div>
      <div class="ebook-text" style="width:220px">Every leader weighs the true cost of keeping service work in house. This guide walks through labor, space, tools and training costs, then compares them with a managed partner so you can see where the savings appear and how quickly they arrive.<br><br>Use the worksheet inside to test your own numbers and build a clear case for your board.</div>
    </div>
    <div class="form">
      <h3>Drop Your Message</h3>
      <div class="field filled"><span>Alex Rowan</span><svg width="14" height="14" viewBox="0 0 14 14" fill="none" stroke="#9aa0a8" stroke-width="1.5"><circle cx="7" cy="4.5" r="3"/><path d="M1.5 13c1-3 10-3 11 0"/></svg></div>
      <div class="field"><span>Phone No</span><svg width="14" height="14" viewBox="0 0 14 14" fill="none" stroke="#9aa0a8" stroke-width="1.5"><path d="M3 1l2.5 3-1.5 1.5c.8 1.8 2.2 3.2 4 4L9.5 8l3 2.5-1.5 2C6 12 2 8 1.5 2.5z"/></svg></div>
      <div class="field"><span>Email Address</span><svg width="14" height="14" viewBox="0 0 14 14" fill="none" stroke="#9aa0a8" stroke-width="1.5"><rect x="1" y="3" width="12" height="9"/><path d="M1 3l6 5 6-5"/></svg></div>
      <div class="field"><span>Question, Comments, Concerns</span><svg width="14" height="14" viewBox="0 0 14 14" fill="none" stroke="#9aa0a8" stroke-width="1.5"><path d="M2 12l1-3 7-7 2 2-7 7z"/></svg></div>
      <a class="btn">LINK TO EBOOK</a>
    </div>
  </div>
</section>

<footer class="site-footer">
  <div class="footer-grid">
    <div>
      <h4>Company</h4>
      <p>It's time to find solutions that deliver more value. Shed the manual interactions that cost you money and distract you from your core.</p>
      <div class="social"><span></span><span></span><span></span><span></span></div>
    </div>
    <div><h4>Links</h4><ul><li>Home</li><li>About Us</li><li>Contact Us</li><li>Markets We Serve</li><li>Apply Today</li></ul></div>
    <div><h4>Other Links</h4><ul><li>Legal</li><li>Our Project</li><li>Privacy Policy</li><li>Terms and conditions</li><li>Privacy Policy</li><li>Contact</li></ul></div>
    <div class="cta"><h3>Take your Business to the next level with Torvenda</h3><a class="btn">Get a Quote</a></div>
  </div>
  <div class="to-top"></div>
  <div class="footer-bar"><span>&copy; Copyright 2020 Torvenda. All Rights Reserved.</span><span>Terms and Conditions &nbsp; Privacy Policy</span></div>
</footer>

</body>
</html>
```